Pelvane Tonic Social Media Graphics

Focusing on the Pelvane Tonic product, create 6-7 individual social media graphics (square size). For the color scheme of the graphics, they should all be complementary with the Pelvane Tonic bottle colors.

Note: each graphic should have one of the 3 pictures of the bottle on it and/or one of the images with a person on it (several pics attached)/only use stock photography that I provided.

Target Market(s)

men and women who need to lose weight

Industry/Entity Type

health and wellness

Colors
A7469A
B969AE
D3A5CF
EDDBEB
F8F0F9

Requirements
Must have
• product pictures
Nice to have
• stock photography that is included

```html
<!DOCTYPE html>
<html lang="en">
<head>
<meta charset="utf-8">
<title>Pelvane Tonic Social Media Graphics</title>
<link rel="stylesheet" href="https://fonts.googleapis.com/css2?family=Poppins:wght@400;500;600;700&display=swap">
<style>
:root{
  --board-grey:#d8d8d8;
  --board-white:#ffffff;
  --plum-deep:#4f1840;
  --plum:#6b3a5e;
  --plum-text:#6b2d5e;
  --magenta:#9a3a8a;
  --orchid:#c77fb2;
  --mauve:#9c5b8e;
  --blush:#eddbeb;
  --mist:#f8f0f9;
  --ink:#1d1d1d;
  --white:#ffffff;
}
*{box-sizing:border-box;margin:0;padding:0}
html,body{width:1200px;height:662px;overflow:hidden}
body{position:relative;font-family:"Poppins",sans-serif;color:var(--ink);background:var(--board-white)}
.board-grey{position:absolute;left:0;top:0;width:623px;height:662px;background:var(--board-grey)}
.post{position:absolute;width:254px;height:254px;background:var(--white);overflow:hidden}
.abs{position:absolute}
.photo{position:absolute}
.bottle{position:absolute;border-radius:6px;background:linear-gradient(180deg,#fafafa 0%,#eeeeee 45%,#e6b9da 80%,#c77fb2 100%)}
.bullets{position:absolute;list-style:none}
.bullets li{position:relative;padding-left:9px;white-space:nowrap}
.bullets li::before{content:"";position:absolute;left:0;top:50%;width:0;height:0;border-left:4px solid currentColor;border-top:2.5px solid transparent;border-bottom:2.5px solid transparent;transform:translateY(-50%)}
.brand{font-weight:600;white-space:nowrap}
.icon-ring{position:absolute;border-radius:50%;display:flex;align-items:center;justify-content:center}
.icon-ring svg{width:55%;height:55%}

/* Post 1 */
.p1{left:41px;top:61px}
.p1 .brand{top:9px;width:100%;text-align:center;font-size:6px;color:var(--plum-text)}
.p1 .headline{top:27px;width:100%;text-align:center;font-size:10.5px;font-weight:600;line-height:15px;color:var(--plum-text)}
.p1 .bullets{left:79px;top:78px;font-size:5px;font-weight:600;color:var(--plum-text);line-height:10.3px}

/* Post 2 */
.p2{left:328px;top:61px}
.p2 .topbar{left:0;top:0;width:254px;height:21px;background:var(--orchid);display:flex;align-items:center;justify-content:space-between;padding:0 16px}
.p2 .topbar .brand{font-size:6.5px;color:var(--white)}
.p2 .phone{display:flex;align-items:center;gap:2px;font-size:4.8px;color:var(--white)}
.p2 .hook{left:51px;top:122px;width:140px;height:17px;background:var(--white);font-size:7.5px;font-weight:600;display:flex;align-items:center;justify-content:center}
.p2 .band{left:0;top:139px;width:254px;height:13px;background:var(--orchid);color:var(--white);font-size:7.3px;font-weight:600;text-align:center;line-height:13px}
.p2 .card{left:107px;top:165px;width:122px;height:70px;border:1px solid var(--orchid);border-radius:7px}
.p2 .bullets{left:123px;top:178px;font-size:5px;font-weight:500;line-height:10.7px}
.p2 .bullets li::before{border:none;width:2.5px;height:2.5px;border-right:0.8px solid var(--ink);border-bottom:0.8px solid var(--ink);transform:translateY(-50%) rotate(-45deg)}

/* Post 3 */
.p3{left:616px;top:61px}
.p3 .column{left:0;top:0;width:129px;height:254px;background:var(--plum)}
.p3 .headline{left:7px;top:14px;font-size:8.8px;font-weight:600;line-height:18.2px;color:var(--white)}
.p3 .row{left:12px;display:flex;align-items:center;gap:3px;font-size:5px;color:var(--white)}
.p3 .row .icon-ring{position:relative;width:21px;height:21px;border:0.8px solid rgba(255,255,255,.75);flex:none}

/* Post 4 */
.p4{left:889px;top:161px}
.p4 .headline{left:13px;top:18px;font-size:12.5px;font-weight:700;line-height:18.2px;color:var(--ink)}
.p4 .benefit{width:90px;text-align:center;font-size:5px;color:var(--white)}
.p4 .icon-ring{width:21px;height:21px;border:0.8px solid rgba(255,255,255,.8)}

/* Post 5 */
.p5{left:41px;top:333px}
.p5 .headline{top:10px;width:100%;text-align:center;font-size:8.8px;font-weight:600;line-height:15px}
.p5 .headline .accent{color:var(--orchid)}
.p5 .label{font-size:5px;text-align:center;width:60px}
.p5 .icon-ring{border:1.5px solid var(--orchid);background:var(--white)}
.p5 .pill{height:12px;border-radius:6px}
.p5 .pill.pink{background:var(--orchid)}
.p5 .pill.grey{background:#e3e3e3}
.p5 .tag{right:0;top:218px;width:62px;height:13px;border-radius:7px 0 0 7px;background:var(--orchid);color:var(--white);font-size:6px;display:flex;align-items:center;justify-content:center}
.p5 .portrait{left:64px;top:112px;width:126px;height:126px;border-radius:50%;border:3px solid var(--orchid);overflow:hidden}

/* Post 6 */
.p6{left:328px;top:333px}
.p6 .headline{left:13px;top:13px;font-size:13px;font-weight:700;line-height:16.3px;color:var(--plum-text)}
.p6 .bullets{left:28px;top:80px;font-size:6.2px;line-height:13px}
.p6 .bullets li::before{border-left-width:3px;border-top-width:2px;border-bottom-width:2px}

/* Post 7 */
.p7{left:616px;top:333px;height:247px}
.p7 .topband{left:0;top:0;width:254px;height:47px;background:var(--mauve);color:var(--white);font-size:10px;text-align:center;line-height:15.5px;padding-top:9px}
.p7 .bullets{left:20px;top:78px;font-size:5px;font-weight:500;line-height:10.7px}
.p7 .bullets li::before{content:"*";border:none;width:auto;height:auto;font-size:6px;top:55%}
.p7 .brand{left:147px;top:196px;width:80px;text-align:center;font-size:6.3px;color:var(--white)}
.p7 .phone{left:155px;top:209px;display:flex;align-items:center;gap:2px;font-size:4.8px;color:var(--white)}
</style>
</head>
<body>
<div class="board-grey"></div>

<!-- Post 1 -->
<section class="post p1">
  <div class="photo" role="img" aria-label="Purple flower petals" style="right:0;top:0;width:38px;height:28px;background:linear-gradient(135deg,#b15ab0,#7a2c8a);border-radius:0 0 0 40px"></div>
  <div class="photo" role="img" aria-label="Purple flower petals" style="left:202px;top:50px;width:38px;height:34px;background:radial-gradient(circle,#9a3fae,#6a1e84);border-radius:50% 40% 50% 45%"></div>
  <div class="photo" role="img" aria-label="Purple flower petals" style="left:228px;top:100px;width:26px;height:34px;background:radial-gradient(circle,#9a3fae,#6a1e84);border-radius:50% 0 0 50%"></div>
  <svg class="abs" style="left:0;top:0" width="254" height="254" viewBox="0 0 254 254">
    <path d="M0 254 L0 248 C90 232 190 190 254 150 L254 254 Z" fill="var(--magenta)"/>
  </svg>
  <p class="abs brand">Pelvane Tonic</p>
  <h1 class="abs headline">Burn Fat Faster: Discover the Simple Detox<br>Your Body Needs</h1>
  <ul class="bullets">
    <li>Melt, especially belly &amp; back fat</li>
    <li>Accelerate overall weight loss</li>
    <li>Boost energy and mental clarity</li>
    <li>Get whiter eyes and glowing skin</li>
  </ul>
  <div class="bottle" role="img" aria-label="Pelvane Tonic supplement bottle" style="left:22px;top:104px;width:70px;height:115px;transform:rotate(-20deg)"></div>
  <div class="photo" role="img" aria-label="Smiling woman in sports bra holding a bathroom scale" style="left:120px;top:126px;width:134px;height:128px;background:linear-gradient(180deg,rgba(120,80,60,.55),rgba(150,150,160,.7) 55%,rgba(60,60,60,.8));border-radius:40% 40% 0 0"></div>
</section>

<!-- Post 2 -->
<section class="post p2">
  <div class="photo" role="img" aria-label="Woman in white sports bra measuring her waist with a tape measure" style="left:0;top:21px;width:254px;height:118px;background:linear-gradient(180deg,#f1eeee 0%,#c9a58e 45%,#8a6e60 80%,#5a5050 100%)"></div>
  <div class="abs topbar">
    <span class="brand">Pelvane Tonic</span>
    <span class="phone"><svg width="9" height="9" viewBox="0 0 10 10"><circle cx="5" cy="5" r="4.4" fill="none" stroke="#fff" stroke-width=".7"/><path d="M3.5 2.8l1 1-.5.6c.3.6.8 1.1 1.4 1.4l.6-.5 1 1-.7.8C4.8 6.8 3.2 5.2 2.8 3.5z" fill="#fff"/></svg>+91 9000012345</span>
  </div>
  <div class="abs hook">Struggling to Lose Weight?</div>
  <div class="abs band">Try This Fat Flush Secret</div>
  <svg class="abs" style="left:11px;top:174px" width="20" height="22" viewBox="0 0 20 22"><path d="M10 2 Q11 10 18 11 Q11 12 10 20 Q9 12 2 11 Q9 10 10 2Z" fill="var(--orchid)"/><path d="M3 2 Q3.4 4 5 4.3 Q3.4 4.6 3 6.5 Q2.6 4.6 1 4.3 Q2.6 4 3 2Z" fill="var(--orchid)"/></svg>
  <div class="bottle" role="img" aria-label="Pelvane Tonic supplement bottle" style="left:36px;top:168px;width:34px;height:80px"></div>
  <div class="abs card"></div>
  <ul class="bullets">
    <li>Melt away stubborn fat</li>
    <li>Accelerate overall weight loss</li>
    <li>Boost energy and mental clarity</li>
    <li>Get whiter eyes and glowing skin</li>
  </ul>
</section>

<!-- Post 3 -->
<section class="post p3">
  <div class="photo" role="img" aria-label="Smiling woman in sports bra holding a bathroom scale" style="left:129px;top:0;width:125px;height:254px;background:linear-gradient(180deg,#e2e2e2 0%,#9a6e55 30%,#b9b9bd 55%,#4a4a4a 100%)"></div>
  <div class="abs column"></div>
  <h2 class="abs headline">Detox and Burn Fat:<br>The 1-Step Solution for a<br>Slimmer You</h2>
  <div class="abs row" style="top:76px"><span class="icon-ring"><svg viewBox="0 0 20 20" fill="none" stroke="#fff" stroke-width="1"><path d="M6 2 Q5 8 7 11 Q5 14 6 18 M14 2 Q15 8 13 11 Q15 14 14 18 M8 9h4"/></svg></span>stubborn fat, especially back fat</div>
  <div class="abs row" style="top:108px"><span class="icon-ring"><svg viewBox="0 0 20 20" fill="none" stroke="#fff" stroke-width="1"><circle cx="10" cy="4" r="2"/><path d="M7 8h6l-1 5h-4zM8.5 13v5M11.5 13v5"/></svg></span>Accelerate overall weight loss</div>
  <div class="abs row" style="top:141px"><span class="icon-ring"><svg viewBox="0 0 20 20" fill="#fff"><path d="M10 3 Q10.6 8 15 8.5 Q10.6 9 10 14 Q9.4 9 5 8.5 Q9.4 8 10 3Z"/><path d="M15 12 Q15.3 14 17 14.3 Q15.3 14.6 15 16.5 Q14.7 14.6 13 14.3 Q14.7 14 15 12Z"/></svg></span>Get whiter eyes and glowing skin</div>
  <div class="bottle" role="img" aria-label="Three Pelvane Tonic supplement bottles" style="left:24px;top:173px;width:75px;height:50px"></div>
</section>

<!-- Post 4 -->
<section class="post p4">
  <div class="photo" role="img" aria-label="Woman in white sports bra with hand on her waist" style="left:0;top:0;width:254px;height:150px;background:linear-gradient(90deg,#cfc6c4 0%,#c7bbb8 45%,#8b6552 75%,#d8d0cf 100%)"></div>
  <svg class="abs" style="left:0;top:0" width="254" height="254" viewBox="0 0 254 254">
    <path d="M0 134 C60 150 150 156 254 134 L254 254 L0 254Z" fill="#000"/>
    <path d="M0 138 C60 156 150 162 254 140 L254 254 L0 254Z" fill="var(--plum-deep)"/>
  </svg>
  <h2 class="abs headline">The Hidden Key to<br>Weight Loss: Liver<br>Health</h2>
  <div class="icon-ring" style="left:43px;top:187px"><svg viewBox="0 0 20 20" fill="none" stroke="#fff" stroke-width="1"><path d="M6 2 Q5 8 7 11 Q5 14 6 18 M14 2 Q15 8 13 11 Q15 14 14 18 M8 9h4"/></svg></div>
  <div class="icon-ring" style="left:117px;top:187px"><svg viewBox="0 0 20 20" fill="none" stroke="#fff" stroke-width="1"><circle cx="10" cy="4" r="2"/><path d="M7 8h6l-1 5h-4zM8.5 13v5M11.5 13v5"/></svg></div>
  <div class="icon-ring" style="left:191px;top:187px"><svg viewBox="0 0 20 20" fill="#fff"><path d="M10 3 Q10.6 8 15 8.5 Q10.6 9 10 14 Q9.4 9 5 8.5 Q9.4 8 10 3Z"/><path d="M15 12 Q15.3 14 17 14.3 Q15.3 14.6 15 16.5 Q14.7 14.6 13 14.3 Q14.7 14 15 12Z"/></svg></div>
  <p class="abs benefit" style="left:8px;top:220px">stubborn fat, especially back fat</p>
  <p class="abs benefit" style="left:82px;top:220px">weight loss</p>
  <p class="abs benefit" style="left:156px;top:220px">Get whiter eyes and glowing skin</p>
</section>

<!-- Post 5 -->
<section class="post p5">
  <h2 class="abs headline">Accelerate Your <span class="accent">Weight Loss With This Easy</span><br>Fat Flush</h2>
  <p class="abs label" style="left:11px;top:78px">stubborn fat</p>
  <p class="abs label" style="left:92px;top:52px">glowing skin</p>
  <p class="abs label" style="left:176px;top:76px">weight loss</p>
  <div class="icon-ring" style="left:21px;top:86px;width:40px;height:40px"><svg viewBox="0 0 20 20" fill="none" stroke="#222" stroke-width=".8"><path d="M6 2 Q5 8 7 11 Q5 14 6 18 M14 2 Q15 8 13 11 Q15 14 14 18 M8 9h4M8 12h4"/></svg></div>
  <div class="icon-ring" style="left:102px;top:61px;width:40px;height:40px"><svg viewBox="0 0 20 20" fill="#222"><path d="M10 3 Q10.6 8 15 8.5 Q10.6 9 10 14 Q9.4 9 5 8.5 Q9.4 8 10 3Z"/><path d="M15 12 Q15.3 14 17 14.3 Q15.3 14.6 15 16.5 Q14.7 14.6 13 14.3 Q14.7 14 15 12Z"/></svg></div>
  <div class="icon-ring" style="left:186px;top:85px;width:40px;height:40px"><svg viewBox="0 0 20 20" fill="none" stroke="#222" stroke-width=".9"><circle cx="10" cy="4" r="2"/><path d="M7 8h6l-1 5h-4zM8.5 13v5M11.5 13v5"/></svg></div>
  <div class="abs pill pink" style="left:-6px;top:152px;width:44px"></div>
  <div class="abs pill grey" style="left:-6px;top:185px;width:34px"></div>
  <div class="abs pill pink" style="left:-6px;top:218px;width:61px"></div>
  <div class="abs pill pink" style="right:-6px;top:152px;width:42px"></div>
  <div class="abs pill grey" style="right:-6px;top:185px;width:32px"></div>
  <div class="abs portrait"><div class="photo" role="img" aria-label="Smiling woman in sports bra holding a bathroom scale" style="inset:0;background:linear-gradient(180deg,#f3f3f3 0%,#9a6e55 40%,#b3b3b8 70%,#555 100%)"></div></div>
  <div class="abs tag brand">Pelvane Tonic</div>
</section>

<!-- Post 6 -->
<section class="post p6">
  <div class="photo" role="img" aria-label="Woman in white sports bra measuring her waist with a yellow tape measure" style="left:95px;top:0;width:159px;height:254px;background:linear-gradient(90deg,rgba(255,255,255,0) 0%,#f0e6e0 40%,#c69478 70%,#eeeeee 100%)"></div>
  <div class="photo" role="img" aria-label="Purple flower petal" style="left:0;top:118px;width:16px;height:26px;background:#8a2f9e;border-radius:0 50% 50% 0"></div>
  <h2 class="abs headline">Cleanse Your Liver,<br>Burn Fat Faster:<br>The Ultimate Solution</h2>
  <ul class="bullets">
    <li>Melt away stubborn fat</li>
    <li>Accelerate overall weight loss</li>
    <li>Boost energy and mental clarity</li>
    <li>Get whiter eyes and glowing skin</li>
  </ul>
  <div class="bottle" role="img" aria-label="Pelvane Tonic supplement bottle" style="left:22px;top:158px;width:52px;height:90px;transform:rotate(-12deg)"></div>
</section>

<!-- Post 7 -->
<section class="post p7">
  <div class="photo" role="img" aria-label="Woman in black sports bra measuring her waist with a tape measure" style="left:0;top:47px;width:254px;height:141px;background:linear-gradient(90deg,#a9c8e0 0%,#8fb0cc 45%,#8a6150 75%,#5a4a48 100%)"></div>
  <div class="abs topband">Flush Away 5-10 Pounds of Toxic Fat in Just<br>Weeks!</div>
  <ul class="bullets">
    <li>Melt away stubborn fat</li>
    <li>Accelerate overall weight loss</li>
    <li>Boost energy and mental clarity</li>
    <li>Get whiter eyes and glowing skin</li>
  </ul>
  <svg class="abs" style="left:0;top:0" width="254" height="247" viewBox="0 0 254 247">
    <path d="M0 167 L254 188 L254 247 L0 247Z" fill="var(--mauve)"/>
    <path d="M22 180 Q23 189 31 190 Q23 191 22 200 Q21 191 13 190 Q21 189 22 180Z" fill="#fff"/>
    <path d="M13 176 Q13.4 178 15 178.3 Q13.4 178.6 13 180.5 Q12.6 178.6 11 178.3 Q12.6 178 13 176Z" fill="#fff"/>
  </svg>
  <div class="bottle" role="img" aria-label="Three Pelvane Tonic supplement bottles" style="left:38px;top:190px;width:73px;height:47px"></div>
  <p class="abs brand">Pelvane Tonic</p>
  <p class="abs phone"><svg width="9" height="9" viewBox="0 0 10 10"><circle cx="5" cy="5" r="4.4" fill="none" stroke="#fff" stroke-width=".7"/><path d="M3.5 2.8l1 1-.5.6c.3.6.8 1.1 1.4 1.4l.6-.5 1 1-.7.8C4.8 6.8 3.2 5.2 2.8 3.5z" fill="#fff"/></svg>+91 9000012345</p>
</section>
</body>
</html>
```